Book Cover for self help book describing how to become the author of your life

I need a good resolution front cover for a book that is published through Brelvox in Print and ebook format. I can design the spine and back cover myself so just need the front angle.
The book is titled "Paint Tomorrow Bright" and it's about writing your own story for how you want to live your life. The image I had in my mind was a pen writing out the title on the front in a script-like font, like actual handwriting.
I've included a very basic mock-up that I've done myself just to give the general idea. The cover requires three pieces of writing.
Title: Paint Tomorrow Bright
Subtitle: Walk Along the Quiet Harbour Path
Author: Martin Folwell
Female 35-55

```html
<!DOCTYPE html>
<html lang="en">
<head>
<meta charset="utf-8">
<title>Paint Tomorrow Bright — Book Cover Wrap</title>
<link rel="stylesheet" href="https://fonts.googleapis.com/css2?family=Great+Vibes&family=Kalam:wght@400&display=swap">
<style>
  :root {
    --backdrop: #ead6ba;
    --paper-light: #f2e3ae;
    --paper-mid: #e0c788;
    --paper-edge: #b99550;
    --ink-black: #161310;
    --ink-blue: #1f2c8c;
    --spine-shade: rgba(90, 60, 20, 0.18);
  }
  * { margin: 0; padding: 0; box-sizing: border-box; }
  html, body {
    width: 1200px;
    height: 864px;
    overflow: hidden;
    background: var(--backdrop);
  }
  .cover-wrap {
    position: absolute;
    left: 60px;
    top: 42px;
    width: 1080px;
    height: 780px;
    display: flex;
  }
  .panel {
    position: relative;
    height: 100%;
    background: radial-gradient(ellipse at 50% 45%, var(--paper-light) 0%, var(--paper-mid) 60%, var(--paper-edge) 100%);
  }
  .back-cover { width: 500px; }
  .spine {
    width: 60px;
    background:
      linear-gradient(90deg, var(--spine-shade), transparent 30%, transparent 70%, var(--spine-shade)),
      radial-gradient(ellipse at 50% 45%, var(--paper-light) 0%, var(--paper-mid) 60%, var(--paper-edge) 100%);
  }
  .front-cover { width: 520px; }

  .script { font-family: "Great Vibes", cursive; font-weight: 400; line-height: 1; }

  .back-title {
    position: absolute;
    left: 0; right: 0; top: 50px;
    text-align: center;
    color: var(--ink-black);
  }
  .back-title .line-small { display: block; font-size: 52px; }
  .back-title .line-large { display: block; font-size: 104px; margin-top: -8px; }

  .back-blurb {
    position: absolute;
    left: 40px;
    top: 290px;
    width: 430px;
    font-family: "Kalam", cursive;
    font-size: 16.5px;
    line-height: 1.28;
    text-align: justify;
    color: var(--ink-black);
    transform: rotate(-3deg);
    transform-origin: left top;
  }

  .spine-text {
    position: absolute;
    left: 50%;
    writing-mode: vertical-rl;
    transform: translateX(-50%);
    color: var(--ink-black);
    white-space: nowrap;
  }
  .spine-title { top: 110px; font-size: 30px; }
  .spine-author { top: 450px; font-size: 26px; }

  .front-title {
    position: absolute;
    left: 0; right: 0; top: 40px;
    text-align: center;
    color: var(--ink-blue);
  }
  .front-title .line-small { display: block; font-size: 64px; }
  .front-title .line-large { display: block; font-size: 140px; margin-top: -10px; }

  .front-subtitle {
    position: absolute;
    left: 30px; right: 30px; top: 345px;
    text-align: center;
    font-size: 50px;
    line-height: 1.05;
    color: var(--ink-blue);
  }

  .front-author {
    position: absolute;
    left: 0; right: 0; bottom: 95px;
    text-align: center;
    font-size: 48px;
    color: var(--ink-blue);
  }
</style>
</head>
<body>
  <main class="cover-wrap">
    <section class="panel back-cover">
      <h2 class="back-title script">
        <span class="line-small">Paint Tomorrow</span>
        <span class="line-large">Bright</span>
      </h2>
      <p class="back-blurb">Lorem Ipsum is simply dummy text of the printing and typesetting industry. Lorem Ipsum has been the industry's standard dummy text ever since the 1500s, when an unknown printer took a galley of type and scrambled it to make a type specimen book. It has survived not only five centuries, but also the leap into electronic typesetting, remaining essentially unchanged. It was popularised in the 1960s with the release of Lettermark sheets containing Lorem Ipsum passages, and more recently with desktop publishing software like Alder PageSmith including versions of Lorem Ipsum.</p>
    </section>

    <section class="panel spine">
      <span class="spine-text spine-title script">Paint Tomorrow Bright</span>
      <span class="spine-text spine-author script">Martin Folwell</span>
    </section>

    <section class="panel front-cover">
      <h1 class="front-title script">
        <span class="line-small">Paint Tomorrow</span>
        <span class="line-large">Bright</span>
      </h1>
      <p class="front-subtitle script">Walk Along the<br>Quiet Harbour Path</p>
      <p class="front-author script">Martin Folwell</p>
    </section>
  </main>
</body>
</html>
```